Web Design Project

Update to the following web page.

www.velorintadvisory.com

We would like a full screen website, similar to the ones found here. http://www.pixelquorra.com/websites/fullscreen/

We also really like this site
http://brightmoleworks.com/

We would like new images and graphics.

Menu should be
1. Audit Defense
2. Education
3. Consulting
4. Outsourcing
5. Our Team
6. Store
7. Contact Us

Incorporate our new logo and colors. File is attached. The blue logo.

We want to add this tag line: "A passion for compliance through homecare and hospice training, education, and consulting."

Target Market(s)

Home Health Care Companies

Industry/Entity Type

Defense

Requirements
Must have
• Display our contact information in header and footer.

```html
<!DOCTYPE html>
<html lang="en">
<head>
<meta charset="utf-8">
<title>Velorint Advisory</title>
<link rel="stylesheet" href="https://fonts.googleapis.com/css2?family=Arimo:wght@400&family=Source+Sans+3:ital,wght@0,400;0,600;1,400&display=swap">
<style>
  :root {
    --page-dark: #141414;
    --header-dark: rgba(10,10,10,0.82);
    --tagline-light: #e6e6e6;
    --tagline-mid: #c9c9c9;
    --text-white: #ffffff;
    --nav-grey: #a8a8a8;
    --brand-blue: #7c93ad;
    --brand-navy: #2c4a6e;
    --search-bg: #3a3a3a;
    --footer-dark: rgba(8,8,8,0.9);
    --copy-grey: #9a9a9a;
    --social-light: #e4e4e4;
  }
  * { box-sizing: border-box; margin: 0; padding: 0; }
  html, body { width: 1200px; height: 720px; overflow: hidden; }
  body {
    position: relative;
    background: var(--page-dark);
    font-family: "Source Sans 3", sans-serif;
    color: var(--text-white);
  }
  .backdrop {
    position: absolute; inset: 0;
    background:
      radial-gradient(ellipse at 55% 45%, #8a8a8a 0%, #4a4a4a 35%, #1e1e1e 70%, #101010 100%);
  }
  .site-header {
    position: absolute; left: 0; top: 0; width: 1200px; height: 173px;
    background: var(--header-dark);
  }
  .tagline-bar {
    position: absolute; left: 47px; top: 0; width: 1106px; height: 29px;
    background: linear-gradient(90deg, var(--tagline-light), var(--tagline-mid));
    color: #1a1a1a; font-style: italic; font-size: 17px;
    line-height: 29px; padding-left: 9px;
  }
  .tagline-close {
    position: absolute; right: 6px; top: 6px; width: 17px; height: 17px;
  }
  .brand {
    position: absolute; left: 56px; top: 45px; height: 117px;
    display: flex; align-items: center;
  }
  .brand-mark {
    width: 26px; height: 26px; background: var(--brand-blue);
    margin-right: 14px;
  }
  .brand-divider {
    width: 2px; height: 117px; background: #333; margin: 0 22px 0 110px;
    position: absolute; left: 24px; top: 0;
  }
  .brand-name {
    margin-left: 136px;
    font-size: 30px; font-weight: 400; color: var(--brand-blue);
    letter-spacing: 1px; white-space: nowrap;
  }
  .search-box {
    position: absolute; left: 909px; top: 52px; width: 235px; height: 23px;
    background: var(--search-bg);
    font-style: italic; font-size: 12px; color: #bbb;
    line-height: 23px; padding-left: 10px;
  }
  .search-icon { position: absolute; right: 4px; top: 3px; width: 18px; height: 17px; }
  .nav {
    display: flex; list-style: none;
    font-family: "Arimo", sans-serif; font-size: 14px; color: var(--nav-grey);
  }
  .nav li + li::before { content: "|"; margin: 0 12px; color: var(--nav-grey); }
  .nav .current { color: var(--text-white); }
  .main-nav { position: absolute; left: 457px; top: 120px; }
  .slider {
    position: absolute; left: 47px; top: 183px; width: 1106px; height: 459px;
    background: radial-gradient(ellipse at 55% 40%, #c9c9c9 0%, #8f8f8f 35%, #4c4c4c 70%, #2a2a2a 100%);
  }
  .slide-copy {
    position: absolute; left: 0; top: 133px; width: 1106px; text-align: center;
    text-shadow: 0 1px 3px rgba(0,0,0,0.5);
  }
  .slide-title { font-size: 34px; font-weight: 400; line-height: 43px; }
  .slide-text { font-size: 18px; line-height: 28px; margin-top: 4px; }
  .slide-link { display: inline-block; font-size: 16px; margin-top: 3px; color: var(--text-white); text-decoration: none; }
  .slide-arrow { position: absolute; top: 206px; width: 47px; height: 47px; }
  .slide-arrow.prev { left: 14px; }
  .slide-arrow.next { right: 14px; }
  .site-footer {
    position: absolute; left: 0; top: 650px; width: 1200px; height: 70px;
    background: var(--footer-dark);
  }
  .footer-nav { position: absolute; left: 56px; top: 16px; }
  .copyright { position: absolute; left: 56px; top: 45px; font-size: 11px; color: var(--copy-grey); }
  .social { position: absolute; left: 1003px; top: 13px; display: flex; gap: 9px; list-style: none; }
  .social li { width: 28px; height: 28px; border-radius: 50%; background: var(--social-light); }
</style>
</head>
<body>
  <div class="backdrop" role="img" aria-label="Blurred full-screen photo of a business meeting in muted greys"></div>

  <header class="site-header">
    <div class="tagline-bar">“A passion for compliance through homecare and hospice training, education, and consulting”
      <svg class="tagline-close" viewBox="0 0 17 17"><circle cx="8.5" cy="8.5" r="8" fill="#111"/><path d="M5.5 5.5l6 6M11.5 5.5l-6 6" stroke="#fff" stroke-width="2"/></svg>
    </div>
    <div class="brand">
      <span class="brand-mark"></span>
      <span class="brand-divider"></span>
      <span class="brand-name">Velorint Advisory</span>
    </div>
    <div class="search-box">Search here...
      <svg class="search-icon" viewBox="0 0 18 17"><circle cx="10.5" cy="7" r="5.5" fill="none" stroke="#111" stroke-width="2"/><path d="M6.5 11L2 15" stroke="#111" stroke-width="2.5" stroke-linecap="round"/></svg>
    </div>
    <ul class="nav main-nav">
      <li class="current">Home</li><li>Audit Defense</li><li>Education</li><li>Consulting</li><li>Outsourcing</li><li>Our Team</li><li>Store</li><li>Contact Us</li>
    </ul>
  </header>

  <section class="slider" role="img" aria-label="Photo of hands holding a printed financial chart and a pen during a meeting">
    <div class="slide-copy">
      <h1 class="slide-title">Lorem Ipsum is simply dummy text of the<br>printing and typesetting industry.</h1>
      <p class="slide-text">Lorem Ipsum has been the industry's standard dummy text ever since the<br>1500s,when an unknown printer took a galley of type and scrambled<br>it to make a type specimen book.</p>
      <a class="slide-link" href="#">Learn more »</a>
    </div>
    <svg class="slide-arrow prev" viewBox="0 0 47 47"><circle cx="23.5" cy="23.5" r="23.5" fill="#d4d4d4"/><path d="M11 23.5L31 12v23z" fill="#111"/></svg>
    <svg class="slide-arrow next" viewBox="0 0 47 47"><circle cx="23.5" cy="23.5" r="23.5" fill="#d4d4d4"/><path d="M36 23.5L16 12v23z" fill="#111"/></svg>
  </section>

  <footer class="site-footer">
    <ul class="nav footer-nav">
      <li class="current">Home</li><li>Audit Defense</li><li>Education</li><li>Consulting</li><li>Outsourcing</li><li>Our Team</li><li>Store</li><li>Contact Us</li>
    </ul>
    <p class="copyright">Copyright © 2013 Velorint Advisory. All Rights Reserved.</p>
    <ul class="social" aria-label="Social links">
      <li></li><li></li><li></li><li></li>
    </ul>
  </footer>
</body>
</html>
```